Corvale Homes

To produce a business card design for our newly established house building and development company, We have had a logo design done please see attached, our slogan is "building your home sweet home"
Contact Information for Business Card
Adress on card needs to Read - 58 Elmsworth Lane, Kettering, Northamptonshire NN16 4QT. Director name Dean Vascotti
Requirements
Must have
- Web adress is www.corvale-homes.co.uk
- Email address is info@corvale-homes.co.uk
- phone number 07700 900417

```html
<!DOCTYPE html>
<html lang="en">
<head>
<meta charset="utf-8">
<title>Corvale Homes – Business Card</title>
<link href="https://fonts.googleapis.com/css2?family=Arimo:wght@400;700&display=swap" rel="stylesheet">
<style>
  :root {
    --page: #d2d2d2;
    --card-light: #e5e5e5;
    --brand-green: #7fb23a;
    --text-grey: #6c6c6c;
    --rule-grey: #8a8a8a;
  }
  * { margin: 0; padding: 0; box-sizing: border-box; }
  html, body {
    width: 1200px; height: 965px; overflow: hidden;
    background: var(--page);
    font-family: "Arimo", Arial, sans-serif;
  }
  .card {
    position: absolute; left: 277px; width: 648px; height: 369px;
  }
  .card-front { top: 97px; background: var(--card-light); }
  .card-back { top: 502px; background: var(--brand-green); }

  .brand {
    position: absolute; display: flex; align-items: center; gap: 10px;
    font-weight: 700; font-size: 30px; letter-spacing: 0.5px; white-space: nowrap;
  }
  .brand-mark { width: 18px; height: 18px; }
  .card-front .brand { left: 42px; top: 88px; color: var(--brand-green); }
  .card-front .brand-mark { background: var(--brand-green); }
  .card-back .brand {
    left: 50%; top: 50%; transform: translate(-50%, -50%);
    color: var(--card-light); font-size: 38px;
  }
  .card-back .brand-mark { background: var(--card-light); width: 22px; height: 22px; }

  .person { position: absolute; left: 42px; top: 214px; }
  .person-name {
    color: var(--brand-green); font-weight: 700; font-size: 21px; letter-spacing: 0.3px;
  }
  .person-role { color: var(--text-grey); font-size: 15px; margin-top: 3px; }

  .divider {
    position: absolute; left: 361px; top: 219px; width: 1.5px; height: 122px;
    background: var(--rule-grey);
  }
  .contact { position: absolute; left: 390px; color: var(--text-grey); font-size: 15px; line-height: 19px; }
  .address { top: 214px; }
  .contact-list { top: 289px; list-style: none; }
  .contact-list li { display: flex; align-items: center; gap: 5px; height: 18.5px; }
  .contact-list svg { width: 13px; height: 13px; flex: none; }
</style>
</head>
<body>
  <section class="card card-front">
    <div class="brand"><span class="brand-mark"></span>Corvale Homes</div>

    <div class="person">
      <div class="person-name">DEAN VASCOTTI</div>
      <div class="person-role">Director</div>
    </div>

    <div class="divider"></div>

    <p class="contact address">58 Elmsworth Lane, Kettering,<br>Northamptonshire NN16 4QT.</p>

    <ul class="contact contact-list">
      <li>
        <svg viewBox="0 0 16 16" fill="none" stroke="#7fb23a" stroke-width="1.8" stroke-linecap="round">
          <path d="M3 2 L6 2 L7 5 L5.5 6.5 Q7 9.5 9.5 10.5 L11 9 L14 10 L14 13 Q8 14 4 9.5 Q2 6 3 2 Z" fill="#7fb23a" stroke-width="1"/>
          <path d="M10 3 Q13 4 13.5 7"/>
        </svg>
        07700 900417
      </li>
      <li>
        <svg viewBox="0 0 16 16" fill="none" stroke="#7fb23a" stroke-width="1.6">
          <rect x="1.5" y="3.5" width="13" height="9"/>
          <path d="M1.5 3.5 L8 9 L14.5 3.5"/>
        </svg>
        info@corvale-homes.co.uk
      </li>
      <li>
        <svg viewBox="0 0 16 16" fill="none" stroke="#7fb23a" stroke-width="1.4">
          <circle cx="8" cy="8" r="6.5"/>
          <ellipse cx="8" cy="8" rx="3" ry="6.5"/>
          <path d="M1.5 8 H14.5 M2.5 4.8 H13.5 M2.5 11.2 H13.5"/>
        </svg>
        www.corvale-homes.co.uk
      </li>
    </ul>
  </section>

  <section class="card card-back">
    <div class="brand"><span class="brand-mark"></span>Corvale Homes</div>
  </section>
</body>
</html>
```